Website for Sports and Exercise Medicine Doctor with active research in stem cells therapies.

I am a sports and exercise medicine doctor with research interests in the cutting edge areas of biological therapies, most notable stem cells. None of my patients are dying of anything, and most of them come to see me to decrease their pain, so they can get back to what they want to do.

The approach i then take is to decrease their pain and support them to achieve the things they wish to achieve. Most people start at "Just make it stop hurting doc" , but I try to move them towards something more important over time.

I would like the website to be very different to other "Doctor or medical websites" in its look. No pictures of doctors in white coats and no pictures of fit old people smiling. I would potentially like the fist thing seen to be a quote:

"Less pain. Everybody wants it, but what are you going to do, once you've got it?"

(But this is only an idea, I am open to anything)

The website will need a couple of things

1. "Locations" I work
2. "Research" I am involved in
3. "Sort Me out" - Clinical information for people to access
4. "Social" - imbedded twitter and facebook
5. "Blog" - imbedded wordpress blog
6. "Bio" - the usual bio-stuff

The "Sort Me out" - pages I would like to have the functionality as seen in this site http://www.veltarion.com.au/platelet/. I intend to put disease topics into these pages (eg Achilles tehdinopathy, osteoarthritis etc etc etc). Once again I am not wedded to this but something along these lines would be good.

To give you an idea these are some sites I like
http://www.morbanquilt.com/
http://daptrine.com/
http://ovimbera.com.sg/
http://jolvaniketchup.com/
http://www.pilnorwave.com/
http://quadrisel.com/#offering
http://fennikstudio.tv/
http://norvalgate.com/
http://sablethorn.co.uk/#about

Target Market(s)

20-80 year old.
People with tendon injuries
People with osteoarthritis
People interested in stem cells
I will build the site over time to contain information on multiple sporting injuries and musculoskeletal disorders. It will also become a site for the latest on stem cell research particularly in the area of osteoarthritis.

Industry/Entity Type

Medical

Font styles to use
Sans Serif

Colors
ffffff

Requirements
Nice to have
• To give you an idea these are some sites I like
http://daptrine.com/
http://fennikstudio.tv/
http://norvalgate.com/
Should not have
• Pictures of doctors in white coats or old fit people smiling

```html
<!DOCTYPE html>
<html lang="en">
<head>
<meta charset="utf-8">
<title>Dr Tomas Welby – Sports and Exercise Medicine</title>
<link rel="stylesheet" href="https://fonts.googleapis.com/css2?family=Roboto:ital,wght@0,300;0,400;0,500;1,300&family=Ruda:wght@400;700&display=swap">
<style>
  :root {
    --red: #c0192b;
    --green: #8cc63f;
    --green-dark: #3fa33a;
    --lime-line: #d9e36a;
    --olive-line: #8a8a2a;
    --ink: #5a5a5a;
    --dark: #232323;
    --white: #ffffff;
    --tweet-bg: #5b5b5b;
    --navy: #1d2a6b;
  }
  * { box-sizing: border-box; margin: 0; padding: 0; }
  html, body { width: 1147px; height: 1200px; overflow: hidden; }
  body {
    position: relative;
    background: var(--dark);
    font-family: "Roboto", Arial, sans-serif;
    color: var(--ink);
  }
  .hero-scene {
    position: absolute; left: 0; top: 0; width: 1147px; height: 680px;
    background: linear-gradient(180deg,
      #bfe3f6 0px, #8fd0f0 120px, #a9d86a 150px, #7cbb2e 200px, #5c9a22 290px,
      #4d6a2a 340px, #54493c 360px, #4a4037 450px, #3b342f 540px, #2a2726 620px, var(--dark) 680px);
  }
  .nav { position: absolute; top: 91px; left: 0; font-family: "Ruda", Arial, sans-serif; font-size: 16.5px; }
  .nav a { position: absolute; color: var(--red); text-decoration: none; white-space: nowrap; }
  .brand {
    position: absolute; left: 515px; top: 0; width: 124px; height: 111px;
    background: var(--white); box-shadow: 0 2px 6px rgba(0,0,0,.35);
    text-decoration: none;
  }
  .brand-dot { position: absolute; left: 41px; top: 30px; width: 42px; height: 42px; border-radius: 50%; background: var(--green); }
  .brand-name { position: absolute; left: 0; right: 0; top: 84px; text-align: center; font-size: 14px; font-weight: 500; color: var(--navy); }
  .social-tabs { position: absolute; left: 1068px; top: 289px; display: flex; }
  .social-tabs a { width: 40px; height: 42px; display: flex; align-items: center; justify-content: center; }
  .social-tabs .tab-a { background: var(--white); border-radius: 4px 0 0 4px; }
  .social-tabs .tab-b { background: var(--green); }
  .social-tabs .tab-a span { width: 18px; height: 18px; border-radius: 50%; background: var(--green); }
  .social-tabs .tab-b span { width: 18px; height: 18px; border-radius: 50%; background: var(--white); }
  .quote { position: absolute; left: 226px; top: 226px; font-size: 51px; line-height: 51px; letter-spacing: -0.3px; text-shadow: 2px 3px 4px rgba(0,0,0,.55); }
  .quote .lead { color: var(--white); text-transform: uppercase; }
  .quote .rest { color: var(--green); }
  .quote-mark { position: absolute; font-family: Georgia, serif; font-weight: 700; font-size: 110px; line-height: 1; color: var(--red); text-shadow: 2px 3px 4px rgba(0,0,0,.4); }
  .card { position: absolute; background: var(--white); }
  .card-title { position: absolute; font-size: 16px; font-weight: 400; color: var(--red); text-transform: uppercase; }
  .rule { position: absolute; height: 2px; background: var(--lime-line); }
  .photo { position: absolute; }
  .body-copy { position: absolute; font-size: 14.7px; font-weight: 300; line-height: 18.4px; color: var(--ink); letter-spacing: .2px; }
  .more { position: absolute; font-size: 11px; color: #8a8a8a; display: flex; align-items: center; gap: 14px; text-decoration: none; }
  .arrow-dot { width: 17px; height: 17px; display: inline-block; }
  .learn-box {
    position: absolute; left: 734px; top: 550px; width: 238px; height: 172px;
    background: var(--green); box-shadow: 2px 3px 6px rgba(0,0,0,.3);
  }
  .learn-box h3 { position: absolute; left: 16px; top: 22px; font-size: 16px; font-weight: 400; color: var(--white); }
  .learn-box ul { position: absolute; left: 16px; top: 54px; list-style: none; }
  .learn-box li { font-size: 15px; font-weight: 300; color: #6f7f66; line-height: 22.5px; display: flex; align-items: center; gap: 8px; }
  .learn-box li::before { content: ""; width: 7px; height: 7px; border-radius: 50%; background: var(--green-dark); }
  .gallery { position: absolute; left: 574px; top: 820px; width: 201px; height: 187px; background: var(--green); }
  .thumb { position: absolute; width: 56px; height: 56px; }
  .view-all { position: absolute; left: 11px; top: 165px; font-size: 12px; color: var(--white); text-decoration: none; }
  .news-title { position: absolute; left: 158px; top: 1031px; font-size: 16px; font-weight: 400; color: var(--red); }
  .news-rule { position: absolute; left: 158px; top: 1056px; width: 363px; height: 1px; background: var(--olive-line); }
  .news-copy { position: absolute; left: 160px; top: 1068px; font-size: 15px; font-weight: 300; line-height: 19px; color: var(--white); letter-spacing: .2px; }
  .tweet { position: absolute; left: 714px; top: 1036px; width: 285px; height: 84px; background: var(--tweet-bg); }
  .tweet::before { content: ""; position: absolute; left: -12px; top: 56px; border: 12px solid transparent; border-left: 0; border-right-color: var(--tweet-bg); }
  .tweet h4 { position: absolute; left: 12px; top: 7px; font-size: 14px; font-weight: 400; color: var(--green); }
  .tweet p { position: absolute; left: 12px; top: 28px; width: 265px; font-size: 12.5px; line-height: 19px; color: #c9c9c9; }
  .tweet-dot { position: absolute; left: 671px; top: 1090px; width: 20px; height: 20px; border-radius: 50%; background: var(--green); }
  .footer { position: absolute; left: 0; top: 1151px; width: 1147px; height: 49px; background: var(--green); font-family: "Ruda", Arial, sans-serif; font-size: 15.5px; }
  .footer a { position: absolute; top: 14px; color: var(--white); text-decoration: none; white-space: nowrap; }
</style>
</head>
<body>
  <div class="hero-scene" role="img" aria-label="Photograph of green grass growing out of dark soil under a blue sky, with a red apple resting on the soil"></div>

  <nav class="nav">
    <a href="#" style="left:281px;">Location</a>
    <a href="#" style="left:369px;">Research</a>
    <a href="#" style="left:463px;">Blog</a>
    <a href="#" style="left:663px;">Sort Me Out</a>
    <a href="#" style="left:779px;">Bio</a>
    <a href="#" style="left:827px;">Social</a>
  </nav>

  <a class="brand" href="#" aria-label="Dr Tomas Welby home">
    <span class="brand-dot"></span>
    <span class="brand-name">Dr Tomas Welby</span>
  </a>

  <div class="social-tabs">
    <a class="tab-a" href="#" aria-label="Follow on social network one"><span></span></a>
    <a class="tab-b" href="#" aria-label="Follow on social network two"><span></span></a>
  </div>

  <div class="quote-mark" style="left:226px;top:176px;">&ldquo;</div>
  <blockquote class="quote">
    <div class="lead">Less pain is like<br>more money.</div>
    <div class="rest">Everybody wants it, but<br>what are you going to<br>do once you've got it?</div>
  </blockquote>
  <div class="quote-mark" style="left:692px;top:478px;">&rdquo;</div>

  <section class="card about" style="left:159px;top:554px;width:841px;height:240px;">
    <h2 class="card-title" style="left:18px;top:18px;">About Us</h2>
    <div class="rule" style="left:15px;top:42px;width:506px;"></div>
    <div class="photo" style="left:28px;top:57px;width:165px;height:160px;background:linear-gradient(160deg,#f4f4f4,#dfe3e8);" role="img" aria-label="Portrait photo of the doctor"></div>
    <p class="body-copy" style="left:222px;top:66px;width:318px;">I am a sports and exercise medicine doctor with research interests in the cutting edge areas of biological therapies, most notable stem cells. None of my patients are dying of anything, and most of them come to see me to decrease their pain, so they can get back to what they want to do</p>
    <a class="more" href="#" style="left:224px;top:201px;">More Information
      <svg class="arrow-dot" viewBox="0 0 17 17" aria-hidden="true"><circle cx="8.5" cy="8.5" r="8.5" fill="#3fa33a"/><path d="M7 5l3.5 3.5L7 12" fill="none" stroke="#fff" stroke-width="2"/></svg>
    </a>
  </section>

  <aside class="learn-box">
    <h3>Learn More</h3>
    <ul>
      <li>Sports and Exercise</li>
      <li>Sports and Exercise</li>
      <li>Sports and Exercise</li>
      <li>Sports and Exercise</li>
    </ul>
  </aside>

  <section class="card blog" style="left:158px;top:820px;width:400px;height:187px;">
    <h2 class="card-title" style="left:17px;top:16px;">Blog</h2>
    <div class="rule" style="left:17px;top:40px;width:364px;"></div>
    <p style="position:absolute;left:18px;top:55px;font-size:12px;font-style:italic;font-weight:300;color:#666;">Sunday 21st April, 2010</p>
    <p class="body-copy" style="left:18px;top:76px;width:372px;">Search interests in the cutting edge areas of bio-<br>logical therapies, most notable stem cells. None of my patients are dying of anything, and most of them come to see me to decrease their pain, so they can</p>
    <a class="more" href="#" style="left:19px;top:154px;">Read More
      <svg class="arrow-dot" viewBox="0 0 17 17" aria-hidden="true"><circle cx="8.5" cy="8.5" r="8.5" fill="#3fa33a"/><path d="M7 5l3.5 3.5L7 12" fill="none" stroke="#fff" stroke-width="2"/></svg>
    </a>
  </section>

  <section class="gallery">
    <h2 class="card-title" style="left:11px;top:16px;">Image Gallery</h2>
    <div class="thumb" style="left:11px;top:39px;background:#d9c8b8;" role="img" aria-label="Gallery photo: hands in a clinic"></div>
    <div class="thumb" style="left:72px;top:39px;background:#1f3f7a;" role="img" aria-label="Gallery photo: blue DNA strand"></div>
    <div class="thumb" style="left:134px;top:39px;background:#5a6f7d;" role="img" aria-label="Gallery photo: laboratory scientist"></div>
    <div class="thumb" style="left:11px;top:102px;background:#c9d3dc;" role="img" aria-label="Gallery photo: microscope"></div>
    <div class="thumb" style="left:72px;top:102px;background:#b8553a;" role="img" aria-label="Gallery photo: medicine bottles and pills"></div>
    <div class="thumb" style="left:134px;top:102px;background:#e6ddd3;" role="img" aria-label="Gallery photo: person exercising"></div>
    <a class="view-all" href="#">View All</a>
  </section>

  <section class="card location" style="left:795px;top:820px;width:200px;height:187px;">
    <h2 class="card-title" style="left:10px;top:16px;">Location</h2>
    <div class="rule" style="left:10px;top:40px;width:172px;"></div>
    <div class="photo" style="left:12px;top:51px;width:176px;height:123px;background:#e3e1dc;" role="img" aria-label="Street map of the clinic location"></div>
  </section>

  <h2 class="news-title">LATEST NEWS</h2>
  <div class="news-rule"></div>
  <p class="news-copy">I am a sports and exercise medicine doctor with research interests<br>in the cutting edge areas of biological therapies, most notable stem</p>

  <span class="tweet-dot" aria-hidden="true"></span>
  <aside class="tweet">
    <h4>LATEST TWEET</h4>
    <p>@loremipsum: lorem ipsum dole ri ma sa m dole ri ma sa m dole ri ma sa</p>
  </aside>

  <footer class="footer">
    <a href="#" style="left:159px;">Location</a>
    <a href="#" style="left:249px;">Research</a>
    <a href="#" style="left:343px;">Blog</a>
    <a href="#" style="left:401px;">Sort Me Out</a>
    <a href="#" style="left:518px;">Bio</a>
    <a href="#" style="left:566px;">Social</a>
    <a href="#" style="left:722px;">Terms &amp; Conditions</a>
    <a href="#" style="left:897px;">Privacy Policy</a>
  </footer>
</body>
</html>
```